Reid Calloway Fitness Business Card

I Need a really cool and creative yet modern and cutting edge. I run a personal training company, I have a logo already which ill submit images of. Id like the base colors to be black and white with a little red as a highlight color. Charcoal grey is fine also. My clientele is mostly comprised of young professionals who are in touch with modern culture art and are interested in "cool" so if there was one thing i want this business card to be it sexy and cool.

Target Market(s)

young professionals who are image conscious, care about their health, looking and feeling good. They know what is cool and expect the best.

Industry/Entity Type

Training

Requirements
Must have
• - must be a 2 sided card
- must include the following:

Reid Calloway CPT
604 392 7715
Reid@ReidCallowayFitness.example
www.ReidCallowayFitness.example
Nice to have
• id like to see some unconventional shape ideas as well as conventional ones

```html
<!DOCTYPE html>
<html lang="en">
<head>
<meta charset="utf-8">
<title>Reid Calloway Fitness – Business Card</title>
<link href="https://fonts.googleapis.com/css2?family=Exo+2:wght@400;500;600&display=swap" rel="stylesheet">
<style>
  :root {
    --frame: #1e1e1e;
    --sheet: #ffffff;
    --card-dark: #232323;
    --card-dark-tone: #2b2b2b;
    --ink: #1a1a1a;
    --rule: #8a8a8a;
    --card-edge: #d9d9d9;
    --accent: #d6001c;
    --on-dark: #ffffff;
  }
  * { margin: 0; padding: 0; box-sizing: border-box; }
  html, body {
    width: 855px; height: 1200px; overflow: hidden;
    background: var(--frame);
    font-family: "Exo 2", "Helvetica Neue", Arial, sans-serif;
  }
  .presentation-sheet {
    position: absolute; left: 30px; top: 31px;
    width: 796px; height: 1138px;
    background: var(--sheet);
    border-radius: 26px;
    overflow: hidden;
  }
  .card {
    position: absolute;
    width: 421px; height: 242px;
    border-radius: 12px;
  }
  /* Front side */
  .card-front {
    left: 196px; top: 269px;
    background: linear-gradient(135deg, var(--card-dark-tone), var(--card-dark));
    color: var(--on-dark);
  }
  .front-brand {
    position: absolute; left: 0; right: 0; top: 108px;
    display: flex; justify-content: center; align-items: center; gap: 10px;
    font-size: 26px; font-weight: 500; letter-spacing: 0.5px;
  }
  .front-brand .brand-dot {
    width: 9px; height: 9px; background: var(--accent);
  }
  .front-web {
    position: absolute; left: 0; right: 0; top: 192px;
    text-align: center;
    font-size: 12.5px; font-weight: 400; letter-spacing: 0.2px;
  }
  /* Back side */
  .card-back {
    left: 203px; top: 576px;
    background: var(--sheet);
    border: 1px solid var(--card-edge);
    color: var(--ink);
  }
  .contact-block {
    position: absolute; right: 199px; top: 66px;
    text-align: right;
  }
  .contact-name {
    font-size: 15.5px; font-weight: 500; color: var(--accent);
    line-height: 1;
  }
  .contact-name .credential { font-size: 11px; }
  .contact-role {
    font-size: 7.5px; font-weight: 600; color: var(--ink);
    margin-top: 3px;
  }
  .contact-phone { font-size: 13px; margin-top: 12px; }
  .contact-email { font-size: 12.4px; margin-top: 7px; }
  .divider {
    position: absolute; left: 243px; top: 45px;
    width: 1px; height: 142px; background: var(--rule);
  }
  .back-brand {
    position: absolute; left: 260px; top: 118px;
  }
  .back-brand-name {
    display: flex; align-items: center; gap: 6px;
    font-size: 12px; font-weight: 500; color: var(--ink);
  }
  .back-brand-name .brand-dot {
    width: 6px; height: 6px; background: var(--accent);
  }
  .back-tagline {
    text-align: right;
    font-size: 7px; font-weight: 500; color: var(--accent);
    margin-top: 2px;
  }
  .services {
    position: absolute; left: 0; right: 0; top: 207px;
    text-align: center;
    font-size: 10.6px; color: var(--ink);
    letter-spacing: 0.1px;
  }
  .services .bullet { color: var(--accent); padding: 0 3px; }
</style>
</head>
<body>
  <main class="presentation-sheet">
    <section class="card card-front" aria-label="Card front">
      <div class="front-brand"><span>Reid Calloway Fitness</span><span class="brand-dot"></span></div>
      <p class="front-web">www.ReidCallowayFitness.example</p>
    </section>

    <section class="card card-back" aria-label="Card back">
      <div class="contact-block">
        <p class="contact-name">Reid Calloway <span class="credential">CPT</span></p>
        <p class="contact-role">Head Trainer</p>
        <p class="contact-phone">604 392 7715</p>
        <p class="contact-email">Reid@ReidCallowayFitness.example</p>
      </div>
      <div class="divider"></div>
      <div class="back-brand">
        <p class="back-brand-name"><span>Reid Calloway Fitness</span><span class="brand-dot"></span></p>
        <p class="back-tagline">Train. Evolve</p>
      </div>
      <p class="services">Body Fat Reduction<span class="bullet">•</span>Toning<span class="bullet">•</span>Strengthening<span class="bullet">•</span>Nutrition<span class="bullet">•</span>Custom Programs</p>
    </section>
  </main>
</body>
</html>
```